New Lead input page design

Attached is our concept of a new lead input screen for the back-end of our website which is a tool for a loan agent (2 page PDF attached)

1. This is the first of many other data input screen projects for our website, so the designer that ends up with us will have quite a bit of add on new projects.

2. HERE IS THE LINK WITH THE SAMPLE OF ALL THE CURRENT CONTROLS:
http://apps.brimtally88.net/controlWidgets.html

3. The colors and hues of: either GREEN & GREYS or BLUE & GREYS.

4. I think some gradients and shadows adds depth and sophistication. Basically trying to get away from old school flat, one dimensional data screen inputs and add some design flare to it.

5. Upon completion we will need the HTML of the design etc and we will code the input fields directly.

6. See attached files for the entire input screen. Please also add the data input space (see sample) to your design.

Thank you

Reason: We are extending the deadline to give us time to ask current designs to complete slight revisions

Reason: Finalizing the selection for one last variation detailed to current designers

```html
<!DOCTYPE html>
<html lang="en">
<head>
<meta charset="utf-8">
<title>Lead Input</title>
<link rel="stylesheet" href="https://fonts.googleapis.com/css2?family=Noto+Sans:wght@400;700&family=Open+Sans:wght@600;700&display=swap">
<style>
:root{
  --brand:#2b78c2;
  --brand-light:#3d8fd9;
  --brand-dark:#1a5a9a;
  --divider:#1b5d9e;
  --page:#e9eaec;
  --card:#ffffff;
  --card-line:#c9ccd1;
  --ink:#1d2228;
  --muted:#5b6470;
  --field:#f7f8fa;
  --field-line:#b9bfc7;
  --link:#1f6fc0;
}
*{margin:0;padding:0;box-sizing:border-box}
html,body{width:1200px;height:895px;overflow:hidden}
body{position:relative;background:var(--page);font-family:Verdana,"Noto Sans",sans-serif;color:var(--ink)}
.top-band{position:absolute;left:0;top:0;width:1200px;height:108px;background:#fff}
.page-texture{position:absolute;left:0;top:108px;width:1200px;height:787px;background:radial-gradient(ellipse at 30% 10%,#f5f6f7 0%,#e6e8eb 55%,#e9eaec 100%)}
.toolbar{position:absolute;left:100px;top:48px;width:1000px;height:60px;background:linear-gradient(#3d8fd9,#2468ab);border-radius:5px 5px 0 0;box-shadow:0 2px 6px rgba(20,50,90,.35)}
.tool{position:absolute;top:0;height:60px;display:flex;align-items:center;gap:8px;color:#fff;font-family:"Open Sans",sans-serif;font-weight:700;font-size:14px;text-shadow:0 1px 1px rgba(0,0,0,.3)}
.tool svg{width:24px;height:24px;flex:none}
.tool-divider{position:absolute;top:8px;width:2px;height:44px;background:var(--divider);box-shadow:1px 0 0 rgba(255,255,255,.25)}
.card{position:absolute;left:100px;width:1001px;height:152px;background:linear-gradient(#ffffff,#f6f7f9);border:1px solid var(--card-line);border-radius:3px;box-shadow:0 2px 5px rgba(40,50,70,.12)}
.badge{position:absolute;left:18px;top:19px;width:112px;height:112px}
.badge-label{font-family:"Open Sans",sans-serif;font-weight:600;fill:#fff;text-anchor:middle}
.fields{position:absolute;left:163px;display:grid;grid-template-columns:183px 209px 196px 220px;grid-auto-rows:30px;font-size:13px;align-items:center}
.label{font-weight:700}
.field{width:190px;height:24px;padding:0 7px;font:13px Verdana,"Noto Sans",sans-serif;color:var(--ink);background:linear-gradient(#ffffff,var(--field));border:1px solid var(--field-line);border-radius:3px;box-shadow:inset 0 1px 2px rgba(0,0,0,.08)}
.field-short{width:150px}
.field-area{height:46px;padding:4px 7px;line-height:18px;resize:none;align-self:start;margin-top:3px}
.with-link{display:flex;align-items:center;gap:6px}
.link{color:var(--link);font-weight:700;text-decoration:underline}
</style>
</head>
<body>
<div class="top-band"></div>
<div class="page-texture" role="img" aria-label="Soft grey background with faint swirl pattern"></div>

<nav class="toolbar">
  <div class="tool" style="left:14px"><svg viewBox="0 0 24 24"><rect x="2" y="2" width="20" height="20" rx="3" fill="#fff" stroke="#0d4d88"/><path d="M9 15l6-6M10 9h5v5" stroke="#2468ab" stroke-width="2" fill="none"/></svg>Lead Category</div>
  <div class="tool-divider" style="left:163px"></div>
  <div class="tool" style="left:178px"><svg viewBox="0 0 24 24"><rect x="2" y="5" width="20" height="17" rx="2" fill="#ffd23a" stroke="#c99600"/><rect x="9" y="1" width="6" height="5" fill="#e33"/></svg>Sticky Note</div>
  <div class="tool-divider" style="left:321px"></div>
  <div class="tool" style="left:350px"><svg viewBox="0 0 24 24"><rect x="2" y="4" width="20" height="16" rx="2" fill="#fff" stroke="#1a4f8a"/><path d="M4 17l5-6 4 4 3-3 4 5z" fill="#2a7fd4"/></svg>Snap Shot</div>
  <div class="tool-divider" style="left:496px"></div>
  <div class="tool" style="left:548px"><svg viewBox="0 0 24 24"><circle cx="12" cy="13" r="9" fill="#fff" stroke="#333" stroke-width="2"/><path d="M12 8v5l3 2" stroke="#c00" stroke-width="2" fill="none"/></svg>Alert</div>
  <div class="tool-divider" style="left:673px"></div>
  <div class="tool" style="left:712px"><svg viewBox="0 0 24 24"><rect x="2" y="3" width="20" height="19" rx="2" fill="#eef3f8" stroke="#8aa"/><circle cx="12" cy="12" r="5" fill="none" stroke="#2a7fd4" stroke-width="2"/></svg>Lead Notes</div>
  <div class="tool-divider" style="left:868px"></div>
  <div class="tool" style="left:889px"><svg viewBox="0 0 24 24"><rect x="2" y="3" width="20" height="19" rx="2" fill="#fff" stroke="#3a5f9a"/><rect x="2" y="3" width="20" height="5" fill="#3a6fb4"/><path d="M5 12h14M5 15h14M5 18h14" stroke="#9ab"/></svg>Calendar</div>
</nav>

<section class="card" style="top:139px">
  <svg class="badge" viewBox="0 0 112 112" aria-hidden="true">
    <defs>
      <linearGradient id="ring" x1="0" y1="0" x2="0" y2="1"><stop offset="0" stop-color="#f4f5f6"/><stop offset=".5" stop-color="#a8adb3"/><stop offset="1" stop-color="#e4e6e8"/></linearGradient>
      <radialGradient id="core" cx=".45" cy=".35" r=".7"><stop offset="0" stop-color="#4a9de6"/><stop offset="1" stop-color="#1b5fa6"/></radialGradient>
    </defs>
    <circle cx="56" cy="56" r="55" fill="url(#ring)" stroke="#979ca3"/>
    <circle cx="56" cy="56" r="45" fill="#134a82"/>
    <circle cx="56" cy="56" r="42" fill="url(#core)" stroke="#6fb3ee"/>
    <text class="badge-label" x="56" y="61" font-size="16">CLIENTS</text>
  </svg>
  <div class="fields" style="top:31px">
    <span class="label">Borrower:</span><input class="field" value="Daniel Harlow"><span class="label">Co-Borrower:</span><input class="field" value="Anna Harlow">
    <span class="label">Application:</span><input class="field" value="Joint"><span class="label">Relationship:</span><input class="field" value="Husband &amp; Wife">
    <span class="label">Laed Stat:</span><span><span class="link">3</span>&nbsp; Demo <span class="link">4</span></span><span class="label">Add Borrowers</span><input class="field" value="N/A">
  </div>
</section>

<section class="card" style="top:320px">
  <svg class="badge" viewBox="0 0 112 112" aria-hidden="true">
    <circle cx="56" cy="56" r="55" fill="url(#ring)" stroke="#979ca3"/>
    <circle cx="56" cy="56" r="45" fill="#134a82"/>
    <circle cx="56" cy="56" r="42" fill="url(#core)" stroke="#6fb3ee"/>
    <text class="badge-label" x="56" y="53" font-size="18">Existing</text>
    <text class="badge-label" x="56" y="75" font-size="18">Loan</text>
  </svg>
  <div class="fields" style="top:16px">
    <span class="label">Current Amount:</span><input class="field" value="$335,758"><span class="label">How many lones:</span><input class="field" value="2  pay off both? yes">
    <span class="label">Current Loan:</span><input class="field" value="30 Year Fix - 5.5%"><span class="label">Current p &amp; I:</span><input class="field" value="$2,200">
    <span class="label">Apprx. Last Refi:</span><input class="field" value="4 Year ago"><span class="label">Tax &amp; Insurance:</span><input class="field" value="$450">
    <span class="label">Add more Lone:</span><input class="field" value="$59,000 - Heloc"><span class="label">Total Payment:</span><input class="field" value="$2,650">
  </div>
</section>

<section class="card" style="top:508px">
  <svg class="badge" viewBox="0 0 112 112" aria-hidden="true">
    <circle cx="56" cy="56" r="55" fill="url(#ring)" stroke="#979ca3"/>
    <circle cx="56" cy="56" r="45" fill="#134a82"/>
    <circle cx="56" cy="56" r="42" fill="url(#core)" stroke="#6fb3ee"/>
    <text class="badge-label" x="56" y="52" font-size="20">New</text>
    <text class="badge-label" x="56" y="77" font-size="20">Loan</text>
  </svg>
  <div class="fields" style="top:31px">
    <span class="label">New Amount:</span><input class="field" value="$336,000"><span class="label">New Loan Purpose:</span><input class="field" value="Rate &amp; Term">
    <span class="label">New Loan:</span><span class="with-link"><input class="field field-short" value="30 Year Fix -"><span class="link">“select”</span></span><span class="label">Closing Costs:</span><input class="field" value="$450">
    <span class="label">Quoted Rate:</span><input class="field" value="5%"><span class="label">Lender credit:</span><input class="field" value="$450">
  </div>
</section>

<section class="card" style="top:698px">
  <svg class="badge" viewBox="0 0 112 112" aria-hidden="true">
    <circle cx="56" cy="56" r="55" fill="url(#ring)" stroke="#979ca3"/>
    <circle cx="56" cy="56" r="45" fill="#134a82"/>
    <circle cx="56" cy="56" r="42" fill="url(#core)" stroke="#6fb3ee"/>
    <text class="badge-label" x="56" y="63" font-size="18">Contact</text>
  </svg>
  <div class="fields" style="top:18px">
    <span class="label">Main Phone:</span><input class="field" value="111-111-1111"><span class="label">Main Phone:</span><input class="field" value="111-111-1111">
    <span class="label">Email:</span><input class="field" value="Daniel@quillpost.net"><span class="label">Email:</span><input class="field" value="Anna@quillpost.net">
    <span class="label">Address:</span><textarea class="field field-area">418 Orbit court
mesa Vale CA 90418</textarea><span class="label">Address:</span><textarea class="field field-area">418 Orbit court
mesa Vale CA 90418</textarea>
  </div>
</section>
</body>
</html>
```